Trovadel Ltda

Logo design focused on: - Construction of civil works - Electrical services - Metal structures - Equipment rental Tomas Ibarra Luque Manager trovadel.ltda@norvexmail.com 56 9 41827035 Quirobamba s / n, Tolvas, San Pedro de Atacama

Target Market(s)

Building

Colors
33a6d7
0292cd
33b8a4
0555a3

```html
<!DOCTYPE html>
<html lang="es">
<head>
<meta charset="utf-8">
<title>Trovadel Ltda – Tarjeta de presentación</title>
<link rel="stylesheet" href="https://fonts.googleapis.com/css2?family=Khand:wght@400;500;600&display=swap">
<style>
  :root {
    --page-bg: #e9e7e3;
    --card-bg: #ffffff;
    --brand-blue: #0555a3;
    --brand-sky: #0292cd;
    --brand-teal: #33b8a4;
    --name-teal: #22aebd;
    --halo: #e3f1f8;
    --ink: #4a4a4a;
    --ink-soft: #5a5a5a;
  }
  * { margin: 0; padding: 0; box-sizing: border-box; }
  html, body { width: 1200px; height: 1200px; overflow: hidden; }
  body {
    background: var(--page-bg);
    font-family: "Khand", "Arial Narrow", sans-serif;
    position: relative;
  }
  .card {
    position: absolute;
    left: 60px; top: 236px;
    width: 1090px; height: 620px;
    background: var(--card-bg);
    border-radius: 300px 4px 4px 300px / 310px 4px 4px 310px;
    overflow: hidden;
    box-shadow: 0 6px 18px rgba(0,0,0,0.12);
  }
  .halo {
    position: absolute;
    left: 266px; top: 32px;
    width: 560px; height: 560px;
    border-radius: 50%;
    background: var(--halo);
    opacity: 0.75;
  }
  .brand {
    position: absolute;
    left: 234px; top: 66px;
    display: flex; align-items: center;
  }
  .brand-dot {
    width: 152px; height: 152px;
    border-radius: 50%;
    background: var(--brand-sky);
  }
  .brand-rule {
    width: 2px; height: 166px;
    background: var(--brand-teal);
    margin: 0 24px 0 38px;
  }
  .brand-name {
    font-weight: 500;
    font-size: 62px;
    letter-spacing: 2px;
    color: var(--brand-blue);
    line-height: 1;
  }
  .details {
    position: absolute;
    left: 0; right: 0; top: 262px;
    text-align: center;
  }
  .person-name {
    font-weight: 600;
    font-size: 50px;
    letter-spacing: 1px;
    color: var(--name-teal);
    line-height: 1;
  }
  .person-role {
    font-weight: 400;
    font-size: 32px;
    color: var(--ink-soft);
    margin-top: 6px;
    line-height: 1;
  }
  .address {
    font-size: 26px;
    color: var(--ink);
    margin-top: 38px;
    line-height: 1;
  }
  .contact {
    display: flex; justify-content: center; align-items: center;
    gap: 18px;
    font-size: 26px;
    color: var(--ink);
    margin-top: 14px;
    line-height: 1;
  }
  .contact-item { display: flex; align-items: center; gap: 8px; }
  .contact-item svg { fill: var(--name-teal); }
  .services {
    font-size: 26px;
    color: var(--ink);
    margin-top: 44px;
    line-height: 1.35;
  }
  .sep { color: var(--name-teal); padding: 0 6px; }
</style>
</head>
<body>
  <section class="card">
    <div class="halo"></div>

    <header class="brand">
      <div class="brand-dot"></div>
      <div class="brand-rule"></div>
      <div class="brand-name">TROVADEL LTDA</div>
    </header>

    <div class="details">
      <h1 class="person-name">TOMAS IBARRA LUQUE</h1>
      <p class="person-role">Gerente</p>
      <p class="address">Quirobamba s/n, Tolvas, San Pedro de Atacama</p>
      <div class="contact">
        <span class="contact-item">
          <svg width="20" height="22" viewBox="0 0 24 24" aria-hidden="true"><path d="M6.6 10.8a15.1 15.1 0 0 0 6.6 6.6l2.2-2.2c.3-.3.7-.4 1-.2 1.1.4 2.3.6 3.6.6.6 0 1 .4 1 1V20c0 .6-.4 1-1 1C10.6 21 3 13.4 3 4c0-.6.4-1 1-1h3.5c.6 0 1 .4 1 1 0 1.3.2 2.5.6 3.6.1.3 0 .7-.2 1z"/></svg>
          +56 9 41827035
        </span>
        <span class="contact-item">
          <svg width="28" height="20" viewBox="0 0 28 20" aria-hidden="true"><path d="M0 0h28v20H0z M2 2v1l12 8 12-8V2z M2 5.5V18h24V5.5l-12 8z" fill-rule="evenodd"/></svg>
          trovadel.ltda@norvexmail.com
        </span>
      </div>
      <p class="services">
        Construcción de Obras Civiles<span class="sep">•</span>Servicios eléctricos<br>
        Estructuras metálicas<span class="sep">•</span>Arriendo de Equipos
      </p>
    </div>
  </section>
</body>
</html>
```